Plumbing Company After Business Card

Business card for a plumbing business that offers a variety of plumbing services including maintenance, domestic and commercial plumbing. My main focus is to offer high quality professional service. A logo on the card would be ideal. Any other questions feel free to email. Cheers

Looking for something modern and upmarket with preferably a matte black background

Business name is Crestline Plumbing and Gas

Industry/Entity Type

Plumbing

Contact Information for Business Card

Crestline Plumbing and Gas
Marcus Thorvale
0472519306
14 Karrabee Drive, Ferndale 3561
crestlineplumbing@mailbay.com.au
ABN 64 915 207 338

Font styles to use
Sans Serif

Colors
1b1b1b
ffffff
3377b5

Requirements
Must have
• Domestic
• Commercial
• Maintenance

```html
<!DOCTYPE html>
<html lang="en">
<head>
<meta charset="utf-8">
<title>Crestline Plumbing and Gas – Business Card</title>
<link rel="stylesheet" href="https://fonts.googleapis.com/css2?family=Lato:wght@400;700&display=swap">
<style>
  :root {
    --stage: #000000;
    --card: #2e2f33;
    --ink: #ffffff;
    --accent: #3377b5;
    --rule: #45464b;
  }
  * { box-sizing: border-box; margin: 0; padding: 0; }
  html, body {
    width: 1200px; height: 900px; overflow: hidden;
    background: var(--stage);
    font-family: "Lato", sans-serif;
  }
  .canvas { position: relative; width: 1200px; height: 900px; }
  .card {
    position: absolute; top: 271px;
    width: 457px; height: 281px;
    background: var(--card);
    border-radius: 14px;
  }
  .card--front { left: 137px; }
  .card--back { left: 626px; }

  /* Front */
  .brand-mark {
    position: absolute; left: 44px; top: 96px; width: 140px;
    display: flex; flex-direction: column; align-items: flex-start; gap: 8px;
  }
  .brand-mark__square { width: 22px; height: 22px; background: var(--accent); }
  .brand-mark__name {
    color: var(--accent); font-weight: 700; font-size: 16px; line-height: 1.2;
  }
  .divider {
    position: absolute; left: 190px; top: 80px;
    width: 1px; height: 140px; background: var(--rule);
  }
  .details { position: absolute; left: 215px; top: 78px; color: var(--ink); }
  .details__name {
    color: var(--accent); font-size: 17px; font-weight: 700; margin-left: -1px;
  }
  .details__address { font-size: 13px; margin-top: 14px; }
  .details__abn { font-size: 13px; margin-top: 15px; }
  .details__abn-label { color: var(--accent); font-weight: 700; }
  .contact { list-style: none; margin-top: 13px; font-size: 13px; }
  .contact__item { display: flex; align-items: center; gap: 12px; height: 20px; }
  .contact__icon { width: 10px; height: 10px; fill: var(--accent); flex: none; }

  /* Back */
  .back-brand {
    position: absolute; left: 0; right: 0; top: 70px;
    display: flex; flex-direction: column; align-items: center; gap: 12px;
  }
  .back-brand__square { width: 34px; height: 34px; background: var(--accent); }
  .back-brand__name {
    width: 280px; text-align: center;
    color: var(--accent); font-weight: 700; font-size: 25px; line-height: 1.15;
    letter-spacing: 0.5px; text-transform: uppercase;
  }
  .services {
    position: absolute; left: 0; right: 0; top: 219px;
    text-align: center; color: var(--ink);
    font-weight: 700; font-size: 15px;
  }
</style>
</head>
<body>
<main class="canvas">
  <section class="card card--front" aria-label="Card front">
    <div class="brand-mark">
      <span class="brand-mark__square"></span>
      <span class="brand-mark__name">Crestline Plumbing and Gas</span>
    </div>
    <div class="divider"></div>
    <div class="details">
      <p class="details__name">Marcus Thorvale</p>
      <p class="details__address">14 Karrabee Drive, Ferndale 3561</p>
      <p class="details__abn"><span class="details__abn-label">ABN:</span> 64 915 207 338</p>
      <ul class="contact">
        <li class="contact__item">
          <svg class="contact__icon" viewBox="0 0 10 10" aria-hidden="true"><path d="M2 0.5 L3.6 2.6 L2.7 3.6 C3.3 5 4.9 6.6 6.4 7.3 L7.4 6.4 L9.5 8 L8.4 9.5 C4.5 9.5 0.5 5.5 0.5 1.6 Z"/></svg>
          <span>0472519306</span>
        </li>
        <li class="contact__item">
          <svg class="contact__icon" viewBox="0 0 10 10" aria-hidden="true"><rect x="0.5" y="2" width="9" height="6.5"/><path d="M1 2.6 L5 5.4 L9 2.6" fill="none" stroke="#2e2f33" stroke-width="0.9"/></svg>
          <span>crestlineplumbing@mailbay.com.au</span>
        </li>
      </ul>
    </div>
  </section>

  <section class="card card--back" aria-label="Card back">
    <div class="back-brand">
      <span class="back-brand__square"></span>
      <span class="back-brand__name">Crestline Plumbing and Gas</span>
    </div>
    <p class="services">Domestic | Commercial | Maintenance</p>
  </section>
</main>
</body>
</html>
```